Marlow Ridge Coffee Product Catalogue 2020

8 page catalogue required
Page 1 Cover Page - MRC logo
Page 2 Coffee/Vending/Powdered - stock image of coffee
Page 3 Syrups - Pellin beverages logo
Page 4 Barista Equipment/Brewing - Quorvin Press logo, tuvel
Page 5 Takeaway cups/lids - Cupwright logo, Fendro Cup logo
Page 6 Tea - the Quiet Kettlehouse logo
Page 7 Equipment and Water filtration - Clarvox, Brunelta, TRV, Stelkin, Il Vantorre and Amber Galley Logos. I need some text space to add a blurb later.
Page 8 Contact Details

all products details on attached Xcel file

Target Market(s)

Local market

Font styles to use
Serif

Colors

Designer to choose colors to be used in the design.

Requirements
Must have
• Page 1 Cover Page - MRC logo
• Page 2 Coffee/Vending/Powdered - stock image of coffee beans.
• Page 3 Syrups - Pellin beverages logo
• Page 4 Barista Equipment/Brewing - Quorvin Press logo, tuvel
• Page 5 Takeaway cups/lids - Cupwright logo, Fendro Cup logo
• Page 6 Tea - the Quiet Kettlehouse logo
• Page 7 Equipment and Water filtration - Clarvox, Brunelta, TRV, Stelkin, Il Vantorre and Amber Galley Logos
• Page 8 Contact Details
• all products details on attached Xcel file
Nice to have
• Industrial feel and look
Should not have
• to much colour

```html
<!DOCTYPE html>
<html lang="en">
<head>
<meta charset="utf-8">
<title>Marlow Ridge Coffee Product Catalogue 2020</title>
<link rel="stylesheet" href="https://fonts.googleapis.com/css2?family=Josefin+Sans:wght@400;600;700&family=Montserrat:wght@400;500;600&display=swap">
<style>
:root{
  --stage-top:#a6a6a6;
  --stage:#8d8d8d;
  --ink:#111111;
  --paper:#ffffff;
  --paper-soft:#f2f2f2;
  --night:#161616;
  --night-soft:#2b2b2b;
  --rule:#1a1a1a;
  --bean-dark:#1e1e1e;
  --bean-mid:#5a5a5a;
}
*{box-sizing:border-box;margin:0;padding:0}
html,body{width:1200px;height:2479px;overflow:hidden}
body{position:relative;background:var(--stage);font-family:"Montserrat",sans-serif;color:var(--ink)}
.stage-top{position:absolute;left:0;top:0;width:1200px;height:885px;background:var(--stage-top)}
.abs{position:absolute}

.card{position:absolute;width:440px;height:318px;overflow:hidden;box-shadow:0 6px 18px rgba(0,0,0,.35)}
.card--front{left:130px;top:270px;background:var(--paper)}
.card--back{left:630px;top:300px;background:var(--night)}

.spread{position:absolute;left:172px;width:861px;display:flex}
.page{position:relative;width:430.5px;height:100%;overflow:hidden;background:var(--paper)}
.page--dark{background:linear-gradient(180deg,var(--night-soft),var(--night))}
.page--left{box-shadow:inset -6px 0 10px -6px rgba(0,0,0,.25)}

.brand{text-align:center;color:var(--ink);font-family:"Josefin Sans",sans-serif;font-weight:700;letter-spacing:.08em;line-height:1.05}
.brand--light{color:var(--paper)}
.brand .mark{display:block;margin:0 auto 5px;width:26px;height:26px;border-radius:50%;background:currentColor}
.web{font-family:"Josefin Sans",sans-serif;letter-spacing:.22em;font-size:8px;text-align:center}
.contact{color:var(--paper);text-align:center;font-size:6px;line-height:1.6}
.contact .name{font-size:9px;letter-spacing:.1em}
.contact .phone{font-size:10px;font-weight:600}
.contact svg{vertical-align:-1px;margin-right:3px}
.socials{display:flex;gap:6px;justify-content:center;margin-top:8px}
.socials span{width:11px;height:11px;border-radius:50%;background:var(--paper)}

.beans{position:absolute;left:0;right:0;bottom:0;background:radial-gradient(ellipse at 40% 100%,var(--bean-dark),var(--bean-mid) 60%,rgba(90,90,90,0) 100%)}
.photo-fade{position:absolute;left:0;right:0;bottom:0}

.section-head{display:flex;align-items:flex-end;justify-content:space-between;border-bottom:1.5px solid var(--rule);font-family:"Josefin Sans",sans-serif;font-weight:700;font-size:11px;letter-spacing:.12em;padding-bottom:1px;white-space:nowrap}
.section-head--compact{font-size:9.5px;letter-spacing:.08em}
.plu{background:var(--ink);color:var(--paper);font-size:5px;padding:2px 6px 1px;border-radius:3px 3px 0 0;letter-spacing:.05em}
.list{list-style:none;margin-top:3px}
.list li{display:grid;grid-template-columns:1fr 28px 22px;font-size:4.3px;line-height:6.4px;letter-spacing:.03em;text-transform:uppercase}
.list li span:nth-child(2),.list li span:nth-child(3){text-align:right}
.block{position:absolute;left:50px;width:180px}

.side-logo{position:absolute;font-family:"Josefin Sans",sans-serif;font-weight:600;font-size:6px;letter-spacing:.06em;color:var(--ink);display:flex;align-items:center;gap:3px;transform:rotate(-90deg);transform-origin:left top;white-space:nowrap}
.side-logo i{width:7px;height:7px;background:var(--ink);display:block}
.pageno{position:absolute;bottom:6px;width:10px;height:6px;background:var(--paper-soft);border:.5px solid #bbb;font-size:3.5px;text-align:center;line-height:6px}

.panel{position:absolute;left:18px;right:18px;background:var(--paper);border-radius:12px}
.panel-title{font-family:"Josefin Sans",sans-serif;font-weight:700;font-size:8px;letter-spacing:.12em;text-align:center;margin-top:8px}
.partners{display:flex;justify-content:space-around;align-items:center;margin-top:14px;padding:0 10px}
.partners span{font-family:"Josefin Sans",sans-serif;font-weight:600;font-size:6.5px;display:flex;align-items:center;gap:3px}
.partners i{width:6px;height:6px;background:var(--ink);display:block}
.writing{font-family:"Josefin Sans",sans-serif;font-size:17px;letter-spacing:.22em;color:#cfcfcf;text-align:center}
</style>
</head>
<body>
<div class="stage-top"></div>

<section class="card card--front">
  <div class="brand abs" style="left:0;right:0;top:46px;font-size:20px"><span class="mark"></span>MARLOW RIDGE<br>COFFEE</div>
  <div class="web abs" style="left:0;right:0;top:142px;color:var(--ink)">www.marlowridgecoffee.com.au</div>
  <div class="beans" style="height:130px" role="img" aria-label="Pile of roasted coffee beans in black and white"></div>
</section>
<section class="card card--back">
  <div class="brand brand--light abs" style="left:0;right:0;top:70px;font-size:11px"><span class="mark" style="width:16px;height:16px"></span>MARLOW RIDGE<br>COFFEE</div>
  <div class="contact abs" style="left:0;right:0;top:130px">
    <div class="name">DANA WHITCOMBE</div>
    <div class="phone"><svg width="7" height="7" viewBox="0 0 10 10"><path d="M2 0h2l1 3-1.5 1a6 6 0 0 0 2.5 2.5L7 5l3 1v2a2 2 0 0 1-2 2A8 8 0 0 1 0 2a2 2 0 0 1 2-2z" fill="#fff"/></svg>0412 908 357</div>
    <div>hello@marlowridgecoffee.com.au</div>
    <div><svg width="6" height="8" viewBox="0 0 10 14"><path d="M5 0a5 5 0 0 1 5 5c0 4-5 9-5 9S0 9 0 5a5 5 0 0 1 5-5z" fill="#fff"/></svg>45 Tannery Lane, Eastwick QLD 4601</div>
    <div>ABN 00 000 000 000</div>
    <div class="socials"><span></span><span></span></div>
  </div>
  <div class="web abs" style="left:0;right:0;bottom:22px;color:var(--paper)">www.marlowridgecoffee.com.au</div>
</section>

<section class="spread" style="top:945px;height:331px">
  <div class="page page--dark page--left">
    <div class="brand brand--light abs" style="left:0;right:0;top:92px;font-size:11px"><span class="mark" style="width:16px;height:16px"></span>MARLOW RIDGE<br>COFFEE</div>
    <div class="contact abs" style="left:0;right:0;top:150px">
      <div class="name">DANA WHITCOMBE</div>
      <div class="phone"><svg width="7" height="7" viewBox="0 0 10 10"><path d="M2 0h2l1 3-1.5 1a6 6 0 0 0 2.5 2.5L7 5l3 1v2a2 2 0 0 1-2 2A8 8 0 0 1 0 2a2 2 0 0 1 2-2z" fill="#fff"/></svg>0412 908 357</div>
      <div>hello@marlowridgecoffee.com.au</div>
      <div><svg width="6" height="8" viewBox="0 0 10 14"><path d="M5 0a5 5 0 0 1 5 5c0 4-5 9-5 9S0 9 0 5a5 5 0 0 1 5-5z" fill="#fff"/></svg>45 Tannery Lane, Eastwick QLD 4601</div>
      <div>ABN 00 000 000 000</div>
      <div class="socials"><span></span><span></span></div>
    </div>
    <div class="web abs" style="left:0;right:0;bottom:22px;color:var(--paper)">www.marlowridgecoffee.com.au</div>
  </div>
  <div class="page">
    <div class="brand abs" style="left:0;right:0;top:40px;font-size:20px"><span class="mark" style="width:30px;height:30px"></span>MARLOW RIDGE<br>COFFEE</div>
    <div class="web abs" style="left:0;right:0;top:150px;color:var(--ink)">www.marlowridgecoffee.com.au</div>
    <div class="beans" style="height:135px" role="img" aria-label="Pile of roasted coffee beans in black and white"></div>
  </div>
</section>

<section class="spread" style="top:1309px;height:336px">
  <div class="page page--left">
    <div class="block" style="top:20px">
      <div class="section-head"><span>COFFEE</span><span class="plu">PLU</span></div>
      <ul class="list">
        <li><span>Ardent Blend Premium 1kg</span><span>$35.00</span><span>4012</span></li>
        <li><span>House Roast 1kg</span><span>$28.00</span><span>4001</span></li>
        <li><span>Ridge Single Origin 1kg</span><span>$29.00</span><span>4002</span></li>
        <li><span>Decaf 1kg</span><span>$32.00</span><span>4020</span></li>
        <li><span>Decaf 250g</span><span>$11.00</span><span>4036</span></li>
        <li><span>Ardent Blend Premium 5kg</span><span>$170.00</span><span>4047</span></li>
        <li><span>House Roast 5kg</span><span>$138.00</span><span>4009</span></li>
        <li><span>Ridge Single Origin 5kg</span><span>$138.00</span><span>4004</span></li>
        <li><span>Decaf Pods Box 50</span><span>$45.00</span><span>4038</span></li>
        <li><span>Specialty origin on request</span><span></span><span></span></li>
      </ul>
    </div>
    <div class="block" style="top:110px">
      <div class="section-head"><span>VENDING PRODUCTS</span><span class="plu">PLU</span></div>
      <ul class="list">
        <li><span>MRC Vending Coffee 400g</span><span>$17.00</span><span>4721</span></li>
        <li><span>MRC Vending Coffee Box 10</span><span>$160.00</span><span>4747</span></li>
        <li><span>MRC Vending Milk 500g</span><span>$12.00</span><span>4725</span></li>
        <li><span>MRC Vending Milk Box 10</span><span>$115.00</span><span>4722</span></li>
        <li><span>MRC Vending Chocolate 1kg</span><span>$12.00</span><span>4711</span></li>
        <li><span>MRC Vending Chocolate Box 12</span><span>$132.00</span><span>4723</span></li>
      </ul>
    </div>
    <div class="photo-fade" style="height:150px;background:linear-gradient(180deg,rgba(255,255,255,0),#9a9a9a 55%,#5c5c5c)" role="img" aria-label="Coffee beans and ground coffee in a scoop, black and white"></div>
    <div class="pageno" style="left:10px">02</div>
  </div>
  <div class="page">
    <div class="side-logo" style="left:8px;top:175px"><i></i>PELLIN BEVERAGES</div>
    <div class="block" style="top:20px;left:55px;width:170px">
      <div class="section-head"><span>SYRUPS</span><span class="plu">PLU</span></div>
      <ul class="list">
        <li><span>Pellin Apple 1L</span><span>$17.00</span><span>4518</span></li>
        <li><span>Pellin Banana Syrup 1L</span><span>$17.00</span><span>4519</span></li>
        <li><span>Pellin Blueberry &amp; Lime 1L</span><span>$17.00</span><span>4517</span></li>
        <li><span>Pellin Butterscotch Syrup 1L</span><span>$15.00</span><span>4500</span></li>
        <li><span>Pellin Caramel Syrup 1L</span><span>$15.00</span><span>4501</span></li>
        <li><span>Pellin Chai Syrup 1L</span><span>$17.00</span><span>4502</span></li>
        <li><span>Pellin Chocolate 1L</span><span>$15.00</span><span>4503</span></li>
        <li><span>Pellin Cranberry &amp; Lime 1L</span><span>$17.00</span><span>4522</span></li>
        <li><span>Pellin Feijoa 1L</span><span>$17.00</span><span>4524</span></li>
        <li><span>Pellin Flamed Orange 1L</span><span>$17.00</span><span>4525</span></li>
        <li><span>Pellin Gold Kiwifruit 1L</span><span>$17.00</span><span>4516</span></li>
        <li><span>Pellin Gomme Sugar Syrup 1L</span><span>$15.00</span><span>4504</span></li>
        <li><span>Pellin Hazelnut Syrup 1L</span><span>$15.00</span><span>4505</span></li>
        <li><span>Pellin Macadamia Syrup 1L</span><span>$15.00</span><span>4506</span></li>
        <li><span>Pellin Mango Syrup 1L</span><span>$17.00</span><span>4507</span></li>
        <li><span>Pellin Manuka Honey 1L</span><span>$22.00</span><span>4526</span></li>
        <li><span>Pellin Passionfruit Syrup 1L</span><span>$17.00</span><span>4508</span></li>
        <li><span>Pellin Peach &amp; Black Tea 1L</span><span>$17.00</span><span>4515</span></li>
        <li><span>Pellin Raspberry 1L</span><span>$17.00</span><span>4509</span></li>
        <li><span>Pellin Rose 1L</span><span>$17.00</span><span>4518</span></li>
        <li><span>Pellin Salted Caramel 1L</span><span>$15.00</span><span>4510</span></li>
        <li><span>Pellin Strawberry Syrup 1L</span><span>$17.00</span><span>4513</span></li>
        <li><span>Pellin Tahitian Lime 1L</span><span>$17.00</span><span>4514</span></li>
        <li><span>Pellin Vanilla Syrup 1L</span><span>$15.00</span><span>4511</span></li>
        <li><span>Pellin White Chocolate 1L</span><span>$15.00</span><span>4512</span></li>
        <li><span>Pellin Wild Peppermint 1L</span><span>$15.00</span><span>4514</span></li>
        <li><span>Pellin Syrup Pump 30ml</span><span>$5.00</span><span>5021</span></li>
        <li><span>Pellin Syrup Pump 20ml</span><span>$5.00</span><span>5022</span></li>
        <li><span>Pellin Syrup Pourer</span><span>$6.00</span><span>5027</span></li>
      </ul>
    </div>
    <div class="pageno" style="right:10px">03</div>
  </div>
</section>

<section class="spread" style="top:1686px;height:331px">
  <div class="page page--left">
    <div class="side-logo" style="left:18px;top:120px"><i></i>QUORVIN PRESS</div>
    <div class="side-logo" style="left:18px;top:200px"><i></i>TUVEL</div>
    <div class="block" style="top:18px;left:58px;width:175px">
      <div class="section-head"><span>BARISTA EQUIPMENT</span><span class="plu">PLU</span></div>
      <ul class="list">
        <li><span>Barista Cloth Hook</span><span>$40.00</span><span>5003</span></li>
        <li><span>Cappuccino Shaker Clear</span><span>$10.00</span><span>5002</span></li>
        <li><span>Cappuccino Shaker Steel</span><span>$20.00</span><span>5001</span></li>
        <li><span>Tamper Station Mat</span><span>$15.00</span><span>5003</span></li>
        <li><span>Espresso Shot Glass</span><span>$8.00</span><span>5032</span></li>
        <li><span>Group Head Brush</span><span>$5.00</span><span>5004</span></li>
        <li><span>Stallo Bag Clip</span><span>$8.00</span><span>5005</span></li>
        <li><span>Stallo Cloth Set</span><span>$15.00</span><span>5007</span></li>
        <li><span>Stallo Cocoa Shaker Fine</span><span>$8.00</span><span>5006</span></li>
        <li><span>Stallo Knock Box Steel</span><span>$68.00</span><span>5028</span></li>
        <li><span>Stallo Milk Pitcher 600ml</span><span>$35.00</span><span>5010</span></li>
        <li><span>Stallo Milk Pitcher 950ml</span><span>$38.00</span><span>5013</span></li>
        <li><span>Stallo Shot Glass Double</span><span>$12.00</span><span>5021</span></li>
        <li><span>Stallo Tamper Classic Mat</span><span>$30.00</span><span>5008</span></li>
        <li><span>Stallo Tamper Mat Corner</span><span>$35.00</span><span>5012</span></li>
        <li><span>Stallo Thermometer 125</span><span>$15.00</span><span>5017</span></li>
        <li><span>Tamper Bench Portafilter</span><span>$18.00</span><span>5015</span></li>
      </ul>
    </div>
    <div class="block" style="top:190px;left:58px;width:175px">
      <div class="section-head"><span>BREWING EQUIPMENT</span><span class="plu">PLU</span></div>
      <ul class="list">
        <li><span>Stallo Dosing Scales</span><span>$50.00</span><span>5514</span></li>
        <li><span>Stallo Travel Mug</span><span>$17.00</span><span>5529</span></li>
        <li><span>Quorvin Coffee Press</span><span>$50.00</span><span>5601</span></li>
        <li><span>Tuvel Drip Scale</span><span>$70.00</span><span>5602</span></li>
        <li><span>Tuvel Paper Filter 100</span><span>$15.00</span><span>5603</span></li>
        <li><span>Tuvel Cold Brew Pot</span><span>$45.00</span><span>5604</span></li>
        <li><span>Tuvel Pour Over Kettle</span><span>$60.00</span><span>5605</span></li>
        <li><span>Tuvel Hand Grinder</span><span>$80.00</span><span>5606</span></li>
        <li><span>Tuvel Cone Dripper</span><span>$30.00</span><span>5607</span></li>
      </ul>
    </div>
    <div class="pageno" style="left:10px">04</div>
  </div>
  <div class="page">
    <div class="side-logo" style="left:10px;top:90px"><i></i>CUPWRIGHT</div>
    <div class="side-logo" style="left:20px;top:170px"><i></i>FENDRO CUP</div>
    <div class="block" style="top:18px;left:55px;width:180px">
      <div class="section-head"><span>TAKEWAY CUPS - HOT</span><span class="plu">PLU</span></div>
      <ul class="list">
        <li><span>MRC Cup 8oz DW Box 1000</span><span>$90.00</span><span>7009</span></li>
        <li><span>MRC Cup 12oz DW Box 1000</span><span>$98.00</span><span>7008</span></li>
        <li><span>Kraft Cup 8oz DW Box 500</span><span>$60.00</span><span>7010</span></li>
        <li><span>Kraft Cup 12oz DW Box 500</span><span>$70.00</span><span>7011</span></li>
        <li><span>Kraft Cup 16oz DW Box 500</span><span>$80.00</span><span>7012</span></li>
        <li><span>Black Cup 8oz DW Box 500</span><span>$60.00</span><span>7014</span></li>
        <li><span>Black Cup 12oz DW Box 500</span><span>$70.00</span><span>7015</span></li>
        <li><span>Black Cup 16oz DW Box 500</span><span>$80.00</span><span>7016</span></li>
      </ul>
    </div>
    <div class="block" style="top:100px;left:55px;width:180px">
      <div class="section-head"><span>TAKEWAY CUPS - COLD</span><span class="plu">PLU</span></div>
      <ul class="list">
        <li><span>Clear Cold Cup 12oz Box 1000</span><span>$140.00</span><span>7065</span></li>
        <li><span>Clear Cold Cup 16oz Box 1000</span><span>$150.00</span><span>7064</span></li>
        <li><span>Clear Cold Cup 20oz Box 1000</span><span>$170.00</span><span>7063</span></li>
      </ul>
    </div>
    <div class="block" style="top:150px;left:55px;width:180px">
      <div class="section-head"><span>TAKEWAY LIDS</span><span class="plu">PLU</span></div>
      <ul class="list">
        <li><span>White Lids 8oz Box 1000</span><span>$50.00</span><span>7101</span></li>
        <li><span>White Lids 12/16oz Box 1000</span><span>$55.00</span><span>7063</span></li>
        <li><span>White Lids 4oz Box 1000</span><span>$49.00</span><span>7062</span></li>
        <li><span>Black Lids 8oz Box 1000</span><span>$52.00</span><span>7103</span></li>
        <li><span>Black Lids 12/16oz Box 1000</span><span>$57.00</span><span>7104</span></li>
        <li><span>Cold Cup Dome Lid Box 1000</span><span>$60.00</span><span>7066</span></li>
        <li><span>Cold Cup Flat Lid Box 1000</span><span>$70.00</span><span>7065</span></li>
      </ul>
    </div>
    <div class="photo-fade" style="height:100px;background:linear-gradient(180deg,rgba(255,255,255,0),#c9c9c9 70%,#a5a5a5)" role="img" aria-label="Faint scattered coffee beans"></div>
    <div class="pageno" style="right:10px">05</div>
  </div>
</section>

<section class="spread" style="top:2074px;height:331px">
  <div class="page page--left">
    <div class="side-logo" style="left:10px;top:150px"><i style="border-radius:50%"></i>QUIET KETTLEHOUSE</div>
    <div class="block" style="top:12px;left:62px;width:200px">
      <div class="section-head section-head--compact"><span>DELUXE PYRAMID TEA BAGS</span><span class="plu">PLU</span></div>
      <ul class="list">
        <li><span>Dark Leaf Black Tea Bag 100</span><span>$35.00</span><span>8510</span></li>
        <li><span>Morning Breakfast Tea Bag 100</span><span>$35.00</span><span>8511</span></li>
        <li><span>Bergamot Grey Tea Bag 100</span><span>$35.00</span><span>8512</span></li>
        <li><span>Sencha Green Tea Bag 100</span><span>$35.00</span><span>8513</span></li>
        <li><span>Spiced Chai Tea Bag 100</span><span>$35.00</span><span>8514</span></li>
        <li><span>Garden Mint Tea Bag 100</span><span>$35.00</span><span>8515</span></li>
      </ul>
    </div>
    <div class="block" style="top:76px;left:62px;width:200px">
      <div class="section-head section-head--compact"><span>PREMIUM LOOSE LEAF TEA</span><span class="plu">PLU</span></div>
      <ul class="list">
        <li><span>Dark Leaf Black 500g</span><span>$28.00</span><span>8520</span></li>
        <li><span>Morning Breakfast 500g</span><span>$28.00</span><span>8521</span></li>
        <li><span>Bergamot Grey 500g</span><span>$28.00</span><span>8522</span></li>
        <li><span>Sencha Green 500g</span><span>$28.00</span><span>8523</span></li>
        <li><span>Spiced Chai 500g</span><span>$28.00</span><span>8524</span></li>
        <li><span>Garden Mint 500g</span><span>$28.00</span><span>8525</span></li>
      </ul>
    </div>
    <div class="block" style="top:140px;left:62px;width:200px">
      <div class="section-head section-head--compact"><span>ICED TEA BASES - LOOSE LEAF</span><span class="plu">PLU</span></div>
      <ul class="list">
        <li><span>Orchard Apple 500g</span><span>$30.00</span><span>8540</span></li>
        <li><span>Berry Hibiscus 500g</span><span>$30.00</span><span>8541</span></li>
        <li><span>Tropical Fruit 500g</span><span>$30.00</span><span>8542</span></li>
      </ul>
    </div>
    <div class="block" style="top:184px;left:62px;width:200px">
      <div class="section-head section-head--compact"><span>TEA ACCESSORIES</span><span class="plu">PLU</span></div>
      <ul class="list">
        <li><span>Large Tea Caddy Silver</span><span>$12.00</span><span>8560</span></li>
        <li><span>Iced Tea Brewer 1L</span><span>$40.00</span><span>8561</span></li>
      </ul>
    </div>
    <div class="block" style="top:222px;left:62px;width:200px">
      <div class="section-head section-head--compact"><span>BUBBLE TEA POPPING BALLS</span><span class="plu">PLU</span></div>
      <ul class="list">
        <li><span>Green Apple Popping Ball Tub 3kg</span><span>$30.00</span><span>8600</span></li>
        <li><span>Lychee Popping Ball Tub 3kg</span><span>$30.00</span><span>8601</span></li>
        <li><span>Mango Popping Ball Tub 3kg</span><span>$30.00</span><span>8602</span></li>
        <li><span>Pomegranate Popping Ball Tub 3kg</span><span>$30.00</span><span>8603</span></li>
      </ul>
    </div>
    <div class="photo-fade" style="height:45px;background:linear-gradient(180deg,rgba(255,255,255,0),#bdbdbd)" role="img" aria-label="Faint tea leaves along the bottom edge"></div>
    <div class="pageno" style="left:10px">06</div>
  </div>
  <div class="page page--dark">
    <div class="panel" style="top:16px;height:80px">
      <div class="panel-title">EQUIPMENT AND WATER FILTRATION</div>
      <div class="partners">
        <span><i></i>Clarvox</span>
        <span>BRUNELTA</span>
        <span><i style="border-radius:50%"></i>TRV</span>
        <span>Stelkin</span>
        <span>Il Vantorre</span>
        <span>amber galley</span>
      </div>
    </div>
    <div class="panel" style="top:106px;height:190px;display:flex;align-items:center;justify-content:center">
      <div class="writing">FOR WRITTING</div>
    </div>
    <div class="web abs" style="right:14px;bottom:8px;font-size:5.5px;color:var(--paper)">www.marlowridgecoffee.com.au</div>
    <div class="pageno" style="left:10px;bottom:8px">07</div>
  </div>
</section>
</body>
</html>
```